Modern Informational OBGYN website

Looking for a modern Wordpress website for a general OBGYN practice in Florida with a specialty in High Risk Obstetrics. We had an old Joomla website that crashed and we lost most of the files. It was over 10 years old and needed a refresh anyway.

Our practice serves a multicultural patient population (white, black, Spanish and Indian) and we would like our website to reflect that diversity. Our company colors are sunshine yellow (#ECBF6D) often combined with black, white and steel blue (#7191BE) in the "life" part of our logo (attached) depending on the background. Our tagline is "We're specialist in You!" Overall the site should have a clean modern yet comfortable feel. One that portrays friendliness and competence. At least 6 pages (Home, Obstetrics, Gynecology, News, Patient Education and Resources). Rotating stock pictures or videos are fine for the headers of the pages if the design you're considering calls for it. Interesting and creative use of typography and icons are encouraged.

The home page should have a call to action to schedule an appointment as well as a link to our patient portal. Other than the home and news pages, the other pages should have a similar look and feel. The home page should have sections on "About Us", "Medical Staff" (with pictures and brief bio for 2 male doctors, 2 female midwives and 1 female nurse practitioner), "Services" and "Location". The news page will be a closed blog that will not allow comments or responses. Both the obstetrics and the gynecology pages will have an educational blurb on the respective topics followed by a list of our services for each topic. Would be nice on the obstetrics page to have information and graphics changes that occur during each trimester (but not necessary). The resource page will have sections on at least "Office Forms", Office Policies", "OB Guide" each with multiple downloadable PDF's. Also a section on "Insurance" with a list of all the major insurance plans that we take with links to their company websites. The address, link and map to our hospital and their website can also go on this page. The Patient Education Page can be broken into 3 sections Obstetrics, Gynecology which both will have definition of medical disorders followed by FAQ's and "Helpful Links" which would have links to other website for medical information.

That's all that I can think of right now. The above is to help guide you but I am flexible, if the website design dictates a better flow of information. Looking forward to seeing what you can come up with. Down the road, I will be looking to the winning designer to produce matching brochures, full, half and quarter page media ads to have on hand for the practices further needs.

Target Market(s)

Women looking medical services

Industry/Entity Type

Medical

Coding

Coded - Design and coding required

Number of Pages Required

5+ page

Font styles to use
Sans Serif
Script

Colors

Designer to choose colors to be used in the design.

Requirements
Must have
• None. See projects description for suggestions
Nice to have
• infographics like information on stages of pregnancy on the obstetrics page

```html
<!DOCTYPE html>
<html lang="en">
<head>
<meta charset="utf-8">
<title>Brightwell Women's Care – OB/GYN</title>
<link href="https://fonts.googleapis.com/css2?family=Playfair+Display:ital,wght@0,700;0,900;1,700&family=Poppins:wght@400;500;600;700;800&display=swap" rel="stylesheet">
<style>
:root{
  --sun:#F3B72C;
  --sun-soft:#F6C94E;
  --steel:#7191BE;
  --steel-news:#809ED0;
  --ink:#1C1C1C;
  --text:#4A4A4A;
  --line:#E6E9EE;
  --white:#FFFFFF;
}
*{margin:0;padding:0;box-sizing:border-box}
html,body{width:1200px;height:4858px;overflow:hidden}
body{font-family:"Poppins",sans-serif;color:var(--ink);background:var(--white);position:relative}
a{color:inherit;text-decoration:none}
.abs{position:absolute}
.serif{font-family:"Playfair Display",serif}
.arrow{display:inline-block;width:14px;height:14px;vertical-align:-2px;margin-left:8px}

/* top bar */
.topbar{position:absolute;top:0;left:0;width:1200px;height:53px;border-bottom:1px solid var(--line);z-index:3;background:rgba(255,255,255,.6)}
.topbar .social{position:absolute;left:92px;top:20px;display:flex;gap:28px}
.topbar .social span{width:12px;height:12px;border-radius:50%;background:var(--ink)}
.topbar .contact{position:absolute;top:16px;font-size:14px;font-weight:500;display:flex;align-items:center;gap:8px}

/* header */
.brand{display:flex;align-items:center;gap:10px}
.brand .dot{width:34px;height:34px;border-radius:50%;background:var(--sun)}
.brand .name{font-weight:700;font-size:28px;color:var(--ink);letter-spacing:.2px}
.header-brand{position:absolute;left:92px;top:84px;z-index:3}
.nav{position:absolute;left:314px;top:92px;display:flex;gap:22px;font-size:15px;font-weight:500;z-index:3}
.portal{position:absolute;left:926px;top:83px;width:180px;height:42px;background:var(--steel);color:#fff;border-radius:4px;font-size:13px;font-weight:600;display:flex;align-items:center;justify-content:center;gap:8px;z-index:3}

/* hero */
.hero{position:absolute;top:0;left:0;width:1200px;height:736px;overflow:hidden;background:linear-gradient(180deg,#EEF3FA 0%,#F7F8F4 55%,#D9E1C6 82%,#B9C79D 100%)}
.hero-photo{position:absolute;left:708px;top:227px;width:640px;height:640px;border-radius:50%;background:radial-gradient(circle at 55% 45%,#F3DCCB 0%,#E8C2A7 40%,#D9D2CC 75%,#C9C3BE 100%)}
.hero-title{position:absolute;left:92px;top:318px}
.hero-title .lead{font-family:"Playfair Display",serif;font-style:italic;font-weight:700;font-size:52px;color:var(--sun);line-height:1}
.hero-title h1{font-family:"Playfair Display",serif;font-weight:900;font-size:72px;line-height:68px;margin-top:10px;letter-spacing:1px}
.btn{display:inline-flex;align-items:center;justify-content:center;font-size:13px;font-weight:600;letter-spacing:.3px;text-transform:uppercase;border-radius:3px}
.hero .btn{position:absolute;left:92px;top:541px;width:287px;height:53px;background:var(--steel);color:#fff}

/* about */
.about{position:absolute;top:736px;left:0;width:1200px;height:632px}
.about .ring{position:absolute;left:94px;top:96px;width:438px;height:438px;border-radius:50%;border:4px solid var(--steel);border-top-color:transparent;transform:rotate(-30deg)}
.about .photo{position:absolute;left:111px;top:113px;width:404px;height:404px;border-radius:50%;background:linear-gradient(135deg,#EDEFF2 0%,#D9DCE0 45%,#8B7467 80%,#4B3A33 100%)}
.about .sun-dot{position:absolute;left:180px;top:94px;width:76px;height:60px;border-radius:38px 38px 0 0;background:var(--sun-soft)}
.section-title{font-weight:800;font-size:40px;letter-spacing:.3px;text-transform:uppercase}
.about h2{position:absolute;left:600px;top:155px}
.about p{position:absolute;left:600px;top:222px;width:520px;font-size:15px;line-height:29.5px;color:var(--text)}
.about .btn{position:absolute;left:600px;top:432px;width:193px;height:53px;background:var(--sun);color:#fff}

/* services */
.services{position:absolute;top:1368px;left:0;width:1200px;height:827px;background:linear-gradient(120deg,#F2B421 0%,#F4BE3C 50%,#F1B52A 100%)}
.services h2{position:absolute;top:122px;width:100%;text-align:center;color:#fff}
.card{position:absolute;top:217px;width:321px;height:415px;background:#fff;border-radius:12px;clip-path:polygon(0 24px,100% 0,100% 100%,0 100%);text-align:center}
.card.active{outline:3px solid var(--steel);outline-offset:-3px}
.card .icon{width:132px;height:132px;border-radius:50%;margin:44px auto 0;background:var(--steel)}
.card .icon.sun{background:var(--sun)}
.card h3{font-family:"Playfair Display",serif;font-style:italic;font-weight:700;font-size:22px;margin-top:38px}
.card p{font-size:16px;line-height:29px;color:var(--text);margin:12px auto 0;width:270px}
.more{display:inline-block;font-size:13px;font-weight:600;text-transform:uppercase;margin-top:20px}
.more.sun{color:var(--sun)}
.more.steel{color:var(--steel)}
.services .btn{position:absolute;left:491px;top:685px;width:217px;height:51px;border:2px solid #fff;color:#fff}

/* staff */
.staff{position:absolute;top:2195px;left:0;width:1200px;height:1211px}
.staff h2{position:absolute;top:122px;width:100%;text-align:center}
.member{position:absolute;width:330px;text-align:center}
.member .portrait{position:relative;width:234px;height:234px;margin:0 auto}
.member .portrait .arc{position:absolute;inset:0;border-radius:50%;border:5px solid var(--sun);border-top-color:transparent;border-right-color:transparent;transform:rotate(10deg)}
.member .portrait .pic{position:absolute;left:17px;top:17px;width:200px;height:200px;border-radius:50%}
.member h3{font-family:"Playfair Display",serif;font-style:italic;font-weight:700;font-size:22px;margin-top:20px}
.member .role{font-size:15px;font-weight:500;margin-top:4px}
.member .bar{width:30px;height:3px;background:var(--sun);margin:8px auto 0}
.member p{font-size:15.5px;line-height:30px;color:var(--text);margin-top:10px}
.member .more{margin-top:16px}
.view-more{position:absolute;left:841px;top:2929px;width:220px;height:220px;border-radius:50%;background:linear-gradient(160deg,#F5C445,#F0AE1E);border:5px solid #fff;box-shadow:0 0 0 4px var(--sun);color:#fff;text-align:center;display:flex;flex-direction:column;justify-content:center}
.view-more .t{font-family:"Playfair Display",serif;font-style:italic;font-weight:700;font-size:25px;line-height:28px}
.view-more .c{font-size:13px;font-weight:600;text-transform:uppercase;margin-top:12px}

/* news */
.news{position:absolute;top:3406px;left:0;width:1200px;height:764px;background:var(--steel-news)}
.news h2{position:absolute;left:92px;top:118px;color:#fff}
.news .btn-all{position:absolute;left:891px;top:129px;width:215px;height:50px;background:var(--sun);color:#fff}
.feature{position:absolute;left:92px;top:234px;width:427px;height:445px;border-radius:10px;overflow:hidden;background:linear-gradient(180deg,#E8E4E0 0%,#C9B8AA 45%,#3C3A3D 100%)}
.feature .date{position:absolute;left:27px;top:285px;background:var(--sun);color:#fff;font-size:13px;padding:3px 10px;border-radius:2px}
.feature h3{position:absolute;left:27px;top:322px;width:380px;color:#fff;font-family:"Playfair Display",serif;font-style:italic;font-weight:700;font-size:21px;line-height:28px}
.feature .more{position:absolute;left:27px;top:400px;margin:0;color:#fff}
.post{position:absolute;left:547px;width:559px;height:210px;background:#fff;border-radius:10px;overflow:hidden}
.post .thumb{position:absolute;left:0;top:0;width:179px;height:100%}
.post .body{position:absolute;left:205px;top:22px;width:335px}
.post h3{font-family:"Playfair Display",serif;font-style:italic;font-weight:700;font-size:18px;line-height:30px}
.post p{font-size:15px;line-height:30px;color:var(--text);margin-top:4px}
.post .more{margin-top:10px}

/* map */
.map{position:absolute;top:4170px;left:0;width:1200px;height:306px;background:linear-gradient(135deg,#ECEEF1 0%,#E2E5EA 50%,#EDEFF1 100%)}
.map-pin{position:absolute;left:542px;top:4286px;width:222px;height:68px;border-radius:34px;background:var(--sun);display:flex;align-items:center;gap:14px;padding-left:8px;color:#fff;font-weight:700;font-size:17px;letter-spacing:1px}
.map-pin .dot{width:52px;height:52px;border-radius:50%;background:#fff}

/* footer */
.footer{position:absolute;top:4476px;left:0;width:1200px;height:382px;background:#fff}
.footer .brand{position:absolute;left:92px;top:130px}
.footer .social{position:absolute;left:92px;top:212px;display:flex;gap:14px}
.footer .social span{width:38px;height:38px;border-radius:50%;border:1.5px solid var(--ink);position:relative}
.footer .social span::after{content:"";position:absolute;left:13px;top:13px;width:9px;height:9px;border-radius:50%;background:var(--ink)}
.footer .copy{position:absolute;left:92px;top:272px;font-size:13px;line-height:24px;color:var(--text)}
.footer .divider{position:absolute;top:122px;width:3px;height:26px;background:var(--sun)}
.fcol{position:absolute;top:122px}
.fcol h4{font-size:18px;font-weight:600}
.fcol ul{list-style:none;margin-top:14px}
.fcol li{font-size:14.5px;line-height:30px}
.contact-row{display:flex;gap:20px;margin-top:16px;font-size:15px;line-height:23px}
.contact-row .ic{flex:none;width:40px;height:40px;border-radius:50%;background:var(--sun);display:flex;align-items:center;justify-content:center}
</style>
</head>
<body>

<!-- hero -->
<section class="hero">
  <div class="hero-photo" role="img" aria-label="Photo of a newborn's feet held in a parent's hands"></div>
  <div class="hero-title">
    <div class="lead">We're</div>
    <h1>SPECIALIST<br>IN YOU</h1>
  </div>
  <a class="btn" href="#">Schedule an appointment
    <svg class="arrow" viewBox="0 0 14 14"><path d="M1 7h11M8 3l4 4-4 4" fill="none" stroke="#fff" stroke-width="1.8"/></svg></a>
</section>

<div class="topbar">
  <div class="social"><span></span><span></span><span></span></div>
  <div class="contact" style="left:704px">
    <svg width="18" height="14" viewBox="0 0 18 14"><rect x="1" y="1" width="16" height="12" rx="2" fill="none" stroke="#1C1C1C" stroke-width="1.6"/><path d="M1.5 2l7.5 6 7.5-6" fill="none" stroke="#1C1C1C" stroke-width="1.6"/></svg>
    username@domain.com</div>
  <div class="contact" style="left:970px">
    <svg width="16" height="16" viewBox="0 0 24 24"><path d="M6.6 10.8a15 15 0 006.6 6.6l2.2-2.2a1 1 0 011-.25 11.4 11.4 0 003.6.6 1 1 0 011 1V20a1 1 0 01-1 1A17 17 0 013 4a1 1 0 011-1h3.5a1 1 0 011 1c0 1.25.2 2.45.6 3.6a1 1 0 01-.25 1z" fill="none" stroke="#1C1C1C" stroke-width="1.8"/></svg>
    123-456-7890</div>
</div>

<header>
  <div class="brand header-brand"><span class="dot"></span><span class="name">Brightwell</span></div>
  <nav class="nav">
    <a href="#">Home</a><a href="#">Obstetrics</a><a href="#">Gynecology</a><a href="#">News</a><a href="#">Patient Education</a><a href="#">Resources</a>
  </nav>
  <a class="portal" href="#">
    <svg width="14" height="14" viewBox="0 0 14 14"><circle cx="7" cy="4.5" r="3" fill="none" stroke="#fff" stroke-width="1.4"/><path d="M1.5 13.5c0-3 2.5-5 5.5-5s5.5 2 5.5 5" fill="none" stroke="#fff" stroke-width="1.4"/></svg>
    PATIENT PORTAL</a>
</header>

<!-- about -->
<section class="about">
  <div class="sun-dot"></div>
  <div class="ring"></div>
  <div class="photo" role="img" aria-label="Photo of a sonographer holding an ultrasound probe"></div>
  <h2 class="section-title">About Us</h2>
  <p>Lorem ipsum dolor sit amet consectetur adipiscing elit, sed do eiusmod tempor incididunt ut labore et dolore magna aliqua se Quis ipsum suspendisse ultrices gravida. Risus commodo ofsho viverra maecenas accumsan lacus vel facilisis of this cities of it Eiusmod tempor incididunt ut labore et dolore magna ullamco laboris nisi ut aliquip ex ea commodo consequat.</p>
  <a class="btn" href="#">More about us
    <svg class="arrow" viewBox="0 0 14 14"><path d="M1 7h11M8 3l4 4-4 4" fill="none" stroke="#fff" stroke-width="1.8"/></svg></a>
</section>

<!-- services -->
<section class="services" role="region" aria-label="Our services">
  <h2 class="section-title">Our Services</h2>
  <article class="card" style="left:92px">
    <div class="icon" role="img" aria-label="Obstetrics icon"></div>
    <h3>Obstetrics</h3>
    <p>Lorem ipsum dolor sit amet consectetur adipiscing elit, sed do eiusmod tempor</p>
    <a class="more sun" href="#">Read more<svg class="arrow" viewBox="0 0 14 14"><path d="M1 7h11M8 3l4 4-4 4" fill="none" stroke="#F3B72C" stroke-width="1.8"/></svg></a>
  </article>
  <article class="card active" style="left:440px">
    <div class="icon sun" role="img" aria-label="Gynecologic care icon"></div>
    <h3>Gynecologic Care</h3>
    <p>Lorem ipsum dolor sit amet consectetur adipiscing elit, sed do eiusmod tempor</p>
    <a class="more steel" href="#">Read more<svg class="arrow" viewBox="0 0 14 14"><path d="M1 7h11M8 3l4 4-4 4" fill="none" stroke="#7191BE" stroke-width="1.8"/></svg></a>
  </article>
  <article class="card" style="left:785px">
    <div class="icon" role="img" aria-label="Birth control icon"></div>
    <h3>Birth Control</h3>
    <p>Lorem ipsum dolor sit amet consectetur adipiscing elit, sed do eiusmod tempor</p>
    <a class="more sun" href="#">Read more<svg class="arrow" viewBox="0 0 14 14"><path d="M1 7h11M8 3l4 4-4 4" fill="none" stroke="#F3B72C" stroke-width="1.8"/></svg></a>
  </article>
  <a class="btn" href="#">View all services
    <svg class="arrow" viewBox="0 0 14 14"><path d="M1 7h11M8 3l4 4-4 4" fill="none" stroke="#fff" stroke-width="1.8"/></svg></a>
</section>

<!-- staff -->
<section class="staff">
  <h2 class="section-title">Medical Staff</h2>
</section>

<div class="member" style="left:80px;top:2406px">
  <div class="portrait"><div class="arc"></div><div class="pic" role="img" aria-label="Portrait photo of Dr. Owen Hartley" style="background:linear-gradient(160deg,#E9ECEF,#B7BCC2)"></div></div>
  <h3>Dr. Owen Hartley</h3><div class="role">Male Doctor</div><div class="bar"></div>
  <p>Lorem ipsum dolor sit amet, consectetur adipiscing elit, sed do eiusmod tempor incididunt ut labore et dolore magna</p>
  <a class="more steel" href="#">Read more<svg class="arrow" viewBox="0 0 14 14"><path d="M1 7h11M8 3l4 4-4 4" fill="none" stroke="#7191BE" stroke-width="1.8"/></svg></a>
</div>
<div class="member" style="left:433px;top:2406px">
  <div class="portrait"><div class="arc"></div><div class="pic" role="img" aria-label="Portrait photo of Dr. Rafael Moreno" style="background:linear-gradient(160deg,#5A5A5C,#2A2A2C)"></div></div>
  <h3>Dr. Rafael Moreno</h3><div class="role">Male Doctor</div><div class="bar"></div>
  <p>Lorem ipsum dolor sit amet, consectetur adipiscing elit, sed do eiusmod tempor incididunt ut labore et dolore magna</p>
  <a class="more steel" href="#">Read more<svg class="arrow" viewBox="0 0 14 14"><path d="M1 7h11M8 3l4 4-4 4" fill="none" stroke="#7191BE" stroke-width="1.8"/></svg></a>
</div>
<div class="member" style="left:786px;top:2406px">
  <div class="portrait"><div class="arc"></div><div class="pic" role="img" aria-label="Portrait photo of midwife Priya Nair" style="background:linear-gradient(160deg,#EDE6E2,#D8C2B3)"></div></div>
  <h3>Priya Nair</h3><div class="role">Midwives</div><div class="bar"></div>
  <p>Lorem ipsum dolor sit amet, consectetur adipiscing elit, sed do eiusmod tempor incididunt ut labore et dolore magna</p>
  <a class="more steel" href="#">Read more<svg class="arrow" viewBox="0 0 14 14"><path d="M1 7h11M8 3l4 4-4 4" fill="none" stroke="#7191BE" stroke-width="1.8"/></svg></a>
</div>
<div class="member" style="left:80px;top:2882px">
  <div class="portrait"><div class="arc"></div><div class="pic" role="img" aria-label="Portrait photo of midwife Keisha D. Laurent" style="background:linear-gradient(160deg,#F0F0F0,#6B4E42)"></div></div>
  <h3>Keisha D. Laurent</h3><div class="role">Midwives</div><div class="bar"></div>
  <p>Lorem ipsum dolor sit amet, consectetur adipiscing elit, sed do eiusmod tempor incididunt ut labore et dolore magna</p>
  <a class="more steel" href="#">Read more<svg class="arrow" viewBox="0 0 14 14"><path d="M1 7h11M8 3l4 4-4 4" fill="none" stroke="#7191BE" stroke-width="1.8"/></svg></a>
</div>
<div class="member" style="left:433px;top:2882px">
  <div class="portrait"><div class="arc"></div><div class="pic" role="img" aria-label="Portrait photo of nurse practitioner Dr. Claire Bennett" style="background:linear-gradient(160deg,#F1EEEA,#D9C9A8)"></div></div>
  <h3>Dr. Claire Bennett</h3><div class="role">Nurse Practitioner</div><div class="bar"></div>
  <p>Lorem ipsum dolor sit amet, consectetur adipiscing elit, sed do eiusmod tempor incididunt ut labore et dolore magna</p>
  <a class="more steel" href="#">Read more<svg class="arrow" viewBox="0 0 14 14"><path d="M1 7h11M8 3l4 4-4 4" fill="none" stroke="#7191BE" stroke-width="1.8"/></svg></a>
</div>
<a class="view-more" href="#">
  <span class="t">View More<br>Medical Staff</span>
  <span class="c">Click here<svg class="arrow" viewBox="0 0 14 14"><path d="M1 7h11M8 3l4 4-4 4" fill="none" stroke="#fff" stroke-width="1.8"/></svg></span>
</a>

<!-- news -->
<section class="news">
  <h2 class="section-title">Latest News</h2>
  <a class="btn btn-all" href="#">View all services
    <svg class="arrow" viewBox="0 0 14 14"><path d="M1 7h11M8 3l4 4-4 4" fill="none" stroke="#fff" stroke-width="1.8"/></svg></a>
  <article class="feature" role="img" aria-label="Photo of a doctor consulting with a patient">
    <span class="date">15 May, 2022</span>
    <h3>Ut enim ad minim veniam quis nostru exercitation ullamco laboris nisi.</h3>
    <a class="more" href="#">Read more<svg class="arrow" viewBox="0 0 14 14"><path d="M1 7h11M8 3l4 4-4 4" fill="none" stroke="#fff" stroke-width="1.8"/></svg></a>
  </article>
  <article class="post" style="top:234px">
    <div class="thumb" role="img" aria-label="Photo of a pregnant woman resting" style="background:linear-gradient(160deg,#DADBD8,#8F9088)"></div>
    <div class="body">
      <h3>Ut enim ad minim veniam quis sedois nostru exercitation ullamco sency</h3>
      <p>Lorem ipsum dolor sit amet, consectetur adipiscing elit, sed do eiusmod tempor..</p>
      <a class="more steel" href="#">Read more<svg class="arrow" viewBox="0 0 14 14"><path d="M1 7h11M8 3l4 4-4 4" fill="none" stroke="#7191BE" stroke-width="1.8"/></svg></a>
    </div>
  </article>
  <article class="post" style="top:472px">
    <div class="thumb" role="img" aria-label="Photo of a doctor examining a pregnant patient" style="background:linear-gradient(160deg,#F1ECEC,#D7A9B4)"></div>
    <div class="body">
      <h3>Ut enim ad minim veniam quis sedois nostru exercitation ullamco sency</h3>
      <p>Lorem ipsum dolor sit amet, consectetur adipiscing elit, sed do eiusmod tempor..</p>
      <a class="more steel" href="#">Read more<svg class="arrow" viewBox="0 0 14 14"><path d="M1 7h11M8 3l4 4-4 4" fill="none" stroke="#7191BE" stroke-width="1.8"/></svg></a>
    </div>
  </article>
</section>

<!-- location -->
<section class="map" role="img" aria-label="Street map showing the clinic location"></section>
<div class="map-pin"><span class="dot"></span>Brightwell</div>

<!-- footer -->
<footer class="footer">
  <div class="brand"><span class="dot"></span><span class="name">Brightwell</span></div>
  <div class="social"><span></span><span></span><span></span></div>
  <div class="copy">Copyright © 2022 Brightwell.<br>All rights reserved.</div>

  <span class="divider" style="left:345px"></span>
  <div class="fcol" style="left:400px">
    <h4>Quick Links</h4>
    <ul><li>Home</li><li>Obstetrics</li><li>Gynecology</li><li>News</li><li>Patient Education</li></ul>
  </div>
  <span class="divider" style="left:572px"></span>
  <div class="fcol" style="left:627px">
    <h4>Helpful Links</h4>
    <ul><li>Insurance</li><li>Office Polies</li><li>Resources</li><li>FAQ</li></ul>
  </div>
  <span class="divider" style="left:817px"></span>
  <div class="fcol" style="left:870px;width:250px">
    <h4>Contact Information</h4>
    <div class="contact-row">
      <span class="ic"><svg width="16" height="18" viewBox="0 0 16 20"><path d="M8 1a6 6 0 016 6c0 4.5-6 12-6 12S2 11.5 2 7a6 6 0 016-6z" fill="#fff"/><circle cx="8" cy="7" r="2.2" fill="#F3B72C"/></svg></span>
      <span>2280 Palm Grove Ave # 210, Coral Shores, FL 33020, United States</span>
    </div>
    <div class="contact-row" style="align-items:center">
      <span class="ic"><svg width="16" height="16" viewBox="0 0 24 24"><path d="M6.6 10.8a15 15 0 006.6 6.6l2.2-2.2a1 1 0 011-.25 11.4 11.4 0 003.6.6 1 1 0 011 1V20a1 1 0 01-1 1A17 17 0 013 4a1 1 0 011-1h3.5a1 1 0 011 1c0 1.25.2 2.45.6 3.6a1 1 0 01-.25 1z" fill="#fff"/></svg></span>
      <span>+15550142087</span>
    </div>
  </div>
</footer>

</body>
</html>
```